the theater production needs a poster design

we
we need a poster design for the Opera 'Tobin and Marigold'
the show will be put on the stage on May 18.
the week is family week.
we launch the Opera on the stage size of 700 people
the opera will be performed by Orchestra of 30 musicians and 7 singers
most of audience are parents with children.
we will use the final design for the printing and mobile marketing.

here is the informations

Opera 'Tobin and Marigold'

date: 2024.5.18 Saturday 2pm, 5pm
Seoryeon Arthall
Ticket $50
BOOK _02-735-6089
Music Director_Yuna Seo, Producer Taeho Park

```html
<!DOCTYPE html>
<html lang="en">
<head>
<meta charset="utf-8">
<title>Tobin &amp; Marigold – Opera Poster</title>
<link rel="stylesheet" href="https://fonts.googleapis.com/css2?family=Jost:wght@500;600;700&display=swap">
<style>
  :root {
    --page-bg: #e4e5e7;
    --poster-bg: #0c0c0e;
    --ink: #ffffff;
    --accent-red: #c8232a;
    --glow-red: #e0452f;
    --photo-dark: #1a1416;
    --photo-red: #b3191f;
    --photo-skin: #8a5a48;
    --photo-floor: #8d8c90;
  }
  html, body {
    margin: 0;
    padding: 0;
    width: 1200px;
    height: 1200px;
    overflow: hidden;
    background: var(--page-bg);
  }
  .poster {
    position: absolute;
    left: 220px;
    top: 62px;
    width: 760px;
    height: 1076px;
    display: block;
  }
  .poster-bg { fill: var(--poster-bg); }
  .opera-letter { fill-rule: evenodd; }
  .opera-fill { fill: url(#dancerTones); }
  .opera-outline { fill: none; stroke: var(--ink); stroke-width: 2.5; stroke-linejoin: miter; }
  .opera-glow { fill: none; stroke: var(--glow-red); stroke-width: 14; opacity: 0.55; }
  .title {
    font-family: "Jost", sans-serif;
    font-weight: 600;
    font-size: 70px;
    fill: var(--ink);
  }
  .details {
    font-family: "Jost", sans-serif;
    font-weight: 600;
    font-size: 29px;
    fill: var(--ink);
  }
  .venue { letter-spacing: 1px; }
  .booking { font-size: 30px; }
  .ticket-band { fill: var(--accent-red); }
  .ticket-price {
    font-family: "Jost", sans-serif;
    font-weight: 600;
    font-size: 62px;
    fill: var(--ink);
  }
  .credits {
    font-family: "Jost", sans-serif;
    font-weight: 500;
    font-size: 20px;
    fill: var(--ink);
  }
</style>
</head>
<body>
<svg class="poster" viewBox="0 0 760 1076" xmlns="http://www.w3.org/2000/svg">
  <defs>
    <linearGradient id="dancerTones" x1="0" y1="0" x2="0" y2="1076" gradientUnits="userSpaceOnUse">
      <stop offset="0" stop-color="var(--photo-dark)"/>
      <stop offset="0.2" stop-color="var(--photo-skin)"/>
      <stop offset="0.35" stop-color="var(--photo-red)"/>
      <stop offset="0.62" stop-color="var(--photo-red)"/>
      <stop offset="0.78" stop-color="var(--photo-dark)"/>
      <stop offset="1" stop-color="var(--photo-floor)"/>
    </linearGradient>
    <filter id="softGlow" x="-30%" y="-30%" width="160%" height="160%">
      <feGaussianBlur stdDeviation="10"/>
    </filter>
    <g id="operaWord">
      <path class="opera-letter" d="M160 58 A89 85 0 1 0 160 228 A89 85 0 1 0 160 58 Z M160 93 A46 50 0 1 1 160 193 A46 50 0 1 1 160 93 Z"/>
      <path class="opera-letter" d="M71 435 V247 H170 A79 57 0 0 1 170 361 H112 V435 Z M112 287 H168 A40 17 0 0 1 168 321 H112 Z"/>
      <path class="opera-letter" d="M71 456 H234 V494 H112 V531 H224 V569 H112 V606 H234 V644 H71 Z"/>
      <path class="opera-letter" d="M71 846 V665 H168 A74 52.5 0 0 1 176 769 L249 846 H202 L136 774 H112 V846 Z M112 703 H166 A34 16 0 0 1 166 735 H112 Z"/>
      <path class="opera-letter" d="M138 869 H182 L249 1025 H204 L191 992 H129 L116 1025 H71 Z M160 912 L181 962 H139 Z"/>
    </g>
  </defs>

  <rect class="poster-bg" x="0" y="0" width="760" height="1076"/>

  <g class="opera-word" role="img" aria-label="Photograph of a dancer in a red dress reaching upward, seen through the letters of OPERA">
    <use href="#operaWord" class="opera-glow" filter="url(#softGlow)"/>
    <use href="#operaWord" class="opera-fill"/>
    <use href="#operaWord" class="opera-outline"/>
  </g>

  <text class="title" x="343" y="234">Tobin</text>
  <text class="title" x="343" y="316">&amp; Marigold</text>

  <text class="details" x="345" y="454">2024.5.18 Saturday</text>
  <text class="details" x="345" y="491">2pm, 5pm</text>
  <text class="details venue" x="345" y="556">SEORYEON ARTHALL</text>

  <rect class="ticket-band" x="308" y="648" width="452" height="94"/>
  <text class="ticket-price" x="345" y="718">Ticket $50</text>

  <text class="details booking" x="345" y="806">BOOK<tspan dx="30">02-735-6089</tspan></text>

  <text class="credits" x="345" y="937">Music Director</text>
  <text class="credits" x="345" y="966">Yuna Seo, Producer Taeho Park</text>
</svg>
</body>
</html>
```